Zielgruppe
Wir sind ein Vertriebsunternehmen, mit dem Ziel die klassische Finanz und den Kryptosektor zu verbinden. Unsere Zielgruppe sind Menschen zwischn 25 - 45 Jahre. Wir sind die Communty und Vertrieb der ersten rechtkonformen STO - Plattform ( Plattform für Wertpapiere im Kryptosektor)
Diese Projekt ist Teil eines Paketes, wir bitten nur Designer mit zu machen die alle benötigten Unterlagen designen können. (siehe restliche Projekte) - Gesamtvolumen: 2300€ Preisgeld
Online-Marketing Material
2 Vorlagen Social Media - (Einladung/Event, Sprüche/Information)
Banner
Präsentationsvorlagen - min unterschiedliche 8 Vorlagenseiten /Layouts.
Landingpage Layout f. Funnelsite für Webinaranmeldung mit Platz für Formular
Newsletter Layoutvorlage
Vorlage Infografik
Broschüre / E - Book Designe
Es werden nur Vorlagen benötigt mit 'LoremSum Texten' und Musterbildern. Wir möchten von allen Vorlagen die Originaldatei, uns stehen folgende Grafikprogramme zur Verfügung:
Adobe Photoshop
Adobe Illustrator
Canva
Newsletter und Landingpage Software: postwelle.com
Unsere Akt. Designe (Designe Alt) gefällt uns von der Idee, dennoch wünschen wir es uns moderner und edler mit ein wenig 'spaceig'. - Eben die Vereinigung von Kryptowelt und klassischer Finanz.
Schriftart: Poppins
Farben lt. Logo
Aufgabenstellung
Die Landingpage Layout f. Funnelsite für Webinaranmeldung mit Platz für Formular - Die Landingpage ersetzt nicht unsere aktuelle Website - sondern dient zur Leadgenerierung im Socialmedia Bereich.

```html
<!DOCTYPE html>
<html lang="de">
<head>
<meta charset="utf-8">
<title>GreenMarten Investments – Webinar-Anmeldung</title>
<link href="https://fonts.googleapis.com/css2?family=Poppins:wght@400;500;600;700&display=swap" rel="stylesheet">
<style>
  :root {
    --navy: #21418f;
    --blue: #2070b2;
    --panel: #e0e0e0;
    --field-line: #7cc3e3;
    --ink: #1c1c1c;
    --white: #ffffff;
    --divider: #d2d2d2;
  }
  * { box-sizing: border-box; margin: 0; padding: 0; }
  html, body { width: 1200px; height: 2398px; overflow: hidden; background: var(--white); }
  body { position: relative; font-family: "Poppins", sans-serif; color: var(--ink); }
  .abs { position: absolute; }

  .top-band { left: 0; top: 0; width: 1200px; height: 47px; background: var(--navy); }
  .hero-photo { left: 0; top: 47px; width: 1200px; height: 162px;
    background: linear-gradient(100deg, #8ea4c4 0%, #c5cfdc 30%, #e6e8ee 55%, #d7dde8 75%, #a9bbd6 100%); }
  .hero-photo-strip { left: 0; top: 357px; width: 1200px; height: 27px;
    background: linear-gradient(100deg, #a9abb8 0%, #c8c9d1 45%, #b4bccb 80%, #8d9ab3 100%); }
  .accent-square { width: 31px; height: 31px; background: var(--blue); }

  .tagline-band { left: 0; top: 209px; width: 1200px; height: 148px; background: var(--white);
    display: flex; align-items: center; justify-content: center; }
  .tagline { font-weight: 700; font-size: 21.5px; color: var(--navy); letter-spacing: -0.2px; margin-left: 44px; }

  .form-panel { left: 160px; top: 384px; width: 880px; height: 1168px; background: var(--panel); }
  .form-header { left: 160px; top: 451px; width: 880px; height: 185px; background: var(--blue); }
  .form-title { left: 219px; top: 486px; font-weight: 600; font-size: 48px; line-height: 57px; color: var(--white); letter-spacing: -0.5px; }
  .form-card { left: 215px; top: 636px; width: 770px; height: 858px; background: var(--white); }

  .field { height: 42px; border: 1px solid var(--field-line); background: var(--white); }
  .select { left: 627px; width: 315px; }
  .select-arrow { position: absolute; right: 0; top: 0; width: 45px; height: 40px; border-left: 1px solid var(--field-line); }
  .column-divider { left: 599px; top: 787px; width: 2px; height: 346px; background: var(--divider); }
  .textarea { left: 264px; top: 1178px; width: 679px; height: 164px; border: 1px solid var(--field-line); }

  .radio { width: 20px; height: 20px; }
  .option-text { font-size: 14.5px; line-height: 18px; }
  .submit-button { left: 579px; top: 1394px; width: 364px; height: 67px; border-radius: 20px; background: var(--blue); border: none; }

  .brand { left: 293px; top: 1597px; height: 70px; display: flex; align-items: center; gap: 14px; }
  .brand-mark { width: 54px; height: 54px; background: var(--blue); }
  .brand-name { font-weight: 700; font-size: 37px; color: var(--navy); letter-spacing: 0.3px; }

  .team-panel { left: 160px; top: 1710px; width: 880px; height: 443px; background: var(--panel); }
  .portrait { width: 148px; height: 148px; border-radius: 50%;
    background: radial-gradient(circle at 50% 40%, #9a9a9a 0%, #5a5a5a 45%, #f2f2f2 46%, #f2f2f2 100%); }
  .member-role { font-size: 16.5px; line-height: 20px; }
  .member-bio { width: 190px; font-size: 16.5px; line-height: 20px; text-align: justify; }
  .intro-text { left: 694px; top: 1782px; width: 299px; font-size: 16.5px; line-height: 20.2px; text-align: justify; hyphens: auto; }
  .team-square { width: 41px; height: 40px; background: var(--blue); }

  .footer-band { left: 0; top: 2153px; width: 1200px; height: 218px; background: var(--navy); }
  .footer-tail { left: 160px; top: 2371px; width: 880px; height: 27px; background: var(--panel); }
</style>
</head>
<body>
  <div class="abs top-band"></div>
  <div class="abs hero-photo" role="img" aria-label="Blue-tinted business photo: hands at a desk with coffee cup, pen and bar-chart printouts"></div>
  <div class="abs accent-square" style="left:918px;top:160px"></div>
  <div class="abs accent-square" style="left:961px;top:160px"></div>
  <div class="abs accent-square" style="left:1005px;top:160px"></div>

  <div class="abs tagline-band">
    <p class="tagline">LOREM IPSUM DOLOR SIT AMET, CONSECTETUER ADIPISCING ELIT, SED</p>
  </div>
  <div class="abs hero-photo-strip" role="img" aria-label="Continuation of the business desk photo"></div>

  <section class="webinar-form">
    <div class="abs form-panel"></div>
    <div class="abs form-header"></div>
    <h1 class="abs form-title">Lorem ipsum<br>dolor sit</h1>
    <div class="abs form-card"></div>

    <div class="abs field" style="left:264px;top:784px;width:314px"></div>
    <div class="abs field" style="left:264px;top:845px;width:314px"></div>
    <div class="abs field" style="left:264px;top:907px;width:314px"></div>
    <div class="abs field" style="left:264px;top:968px;width:314px"></div>
    <div class="abs field" style="left:264px;top:1029px;width:167px"></div>
    <div class="abs field" style="left:438px;top:1029px;width:140px"></div>
    <div class="abs field" style="left:264px;top:1091px;width:314px"></div>

    <div class="abs column-divider"></div>

    <div class="abs field select" style="top:784px">
      <svg class="select-arrow" viewBox="0 0 45 40"><path d="M7 14 H37 L22 30 Z" fill="#333"/></svg>
    </div>
    <div class="abs field select" style="top:845px">
      <svg class="select-arrow" viewBox="0 0 45 40"><path d="M7 14 H37 L22 30 Z" fill="#333"/></svg>
    </div>

    <svg class="abs radio" style="left:629px;top:958px" viewBox="0 0 20 20">
      <defs><radialGradient id="rb1" cx="40%" cy="35%" r="65%"><stop offset="0" stop-color="#f2f5f8"/><stop offset="1" stop-color="#8a96a3"/></radialGradient></defs>
      <circle cx="10" cy="10" r="9.5" fill="#dfe3e7" stroke="#aab2bb"/>
      <circle cx="10" cy="10" r="6" fill="url(#rb1)"/>
    </svg>
    <p class="abs option-text" style="left:657px;top:956px;width:290px">Lorem ipsum dolor sit amet, consectetuer adipiscing elit, sed diam no</p>

    <div class="abs textarea"></div>

    <p class="abs option-text" style="left:263px;top:1399px;width:250px;text-align:right">Lorem ipsum dolor sit amet, consectetuer adipiscing elit, sed diam no</p>
    <svg class="abs radio" style="left:525px;top:1400px" viewBox="0 0 20 20">
      <defs><radialGradient id="rb2" cx="40%" cy="35%" r="65%"><stop offset="0" stop-color="#f2f5f8"/><stop offset="1" stop-color="#8a96a3"/></radialGradient></defs>
      <circle cx="10" cy="10" r="9.5" fill="#dfe3e7" stroke="#aab2bb"/>
      <circle cx="10" cy="10" r="6" fill="url(#rb2)"/>
    </svg>
    <div class="abs submit-button"></div>
  </section>

  <div class="abs brand">
    <div class="brand-mark"></div>
    <span class="brand-name">GREENMARTEN INVESTMENTS</span>
  </div>

  <section class="team">
    <div class="abs team-panel"></div>
    <div class="abs portrait" style="left:222px;top:1774px" role="img" aria-label="Black-and-white portrait of a team member in a suit"></div>
    <p class="abs member-role" style="left:405px;top:1774px">Lorem ipsum</p>
    <p class="abs member-bio" style="left:407px;top:1817px">Lorem ipsum dolor sit amet, consectetuer adipiscing elit, sed diam nonummy nibh euismod tincidunt ut</p>

    <div class="abs portrait" style="left:222px;top:1974px" role="img" aria-label="Black-and-white portrait of a second team member in a suit"></div>
    <p class="abs member-role" style="left:405px;top:1973px">Lorem ipsum</p>
    <p class="abs member-bio" style="left:405px;top:2016px">Lorem ipsum dolor sit amet, consectetuer adipiscing elit, sed diam nonummy nibh euismod tincidunt ut</p>

    <p class="abs intro-text">Lorem ipsum dolor sit amet, con­sectetuer adipiscing elit, sed diam nonummy nibh euismod tincidunt ut laoreet dolore magna aliquam erat volutpat. Ut wisi enim ad minim veniam, quis nostrud exerci tation ullamcorper suscipit lobortis nisl ut aliquip ex ea commodo consequat. Duis autem vel eum iriure dolor in hendrerit in vulputate velit esse mo­lestie consequat, vel illum dolore eu feugiat nulla facilisis at vero</p>
    <div class="abs team-square" style="left:840px;top:2070px"></div>
    <div class="abs team-square" style="left:896px;top:2070px"></div>
  </section>

  <div class="abs footer-band"></div>
  <div class="abs footer-tail"></div>
</body>
</html>
```